Small rum distillery looking for bottle design

Small rum distillery in Estonia. Looking for bottle lable design. It should be simple but at the same time point out from the variety of other bottles.
As we are a small nordic country, design can be some how nordic or represent our country. It can also have some connection with sailing or sea as we know it pirates love it.
Bottle we are using is Corvane 540

Industry/Entity Type

food and beverage

Other font styles liked:
• Baskerville

```html
<!DOCTYPE html>
<html lang="en">
<head>
<meta charset="utf-8">
<title>Halmar Distillery – Handcrafted Rum Label</title>
<link rel="stylesheet" href="https://fonts.googleapis.com/css2?family=EB+Garamond:wght@400;500;600;700&display=swap">
<style>
  :root {
    --page: #f3f3f0;
    --label: #ffffff;
    --ink: #4a4a4c;
    --ink-soft: #5a5a5c;
    --red: #c23b3c;
    --rule-red: #d58a8a;
    --ship: #e4e6e0;
    --faint: #d9d9d9;
  }
  * { margin: 0; padding: 0; box-sizing: border-box; }
  html, body {
    width: 1200px; height: 849px; overflow: hidden;
    background: var(--page);
    font-family: "EB Garamond", Georgia, serif;
    color: var(--ink);
  }
  .label {
    position: absolute; left: 165px; top: 45px;
    width: 870px; height: 760px;
    background: var(--label);
    box-shadow: 0 2px 10px rgba(0,0,0,0.08);
    overflow: hidden;
  }
  .label__band {
    position: absolute; left: 0; top: 0; width: 100%; height: 11px;
    background: var(--red);
  }
  .label__scene {
    position: absolute; left: 10px; top: 205px; width: 830px; height: 336px;
    background: radial-gradient(ellipse at 50% 45%, var(--ship) 0%, rgba(228,230,224,0.55) 45%, rgba(255,255,255,0) 72%);
  }
  .brand-mark {
    position: absolute; left: 0; top: 140px; width: 100%;
    display: flex; justify-content: center; align-items: center; gap: 12px;
  }
  .brand-mark__dot {
    width: 22px; height: 22px; border-radius: 50%; background: var(--red);
  }
  .brand-mark__name {
    font-size: 22px; font-weight: 500; letter-spacing: 6px; color: var(--red);
  }
  .wordmark {
    position: absolute; left: 0; top: 262px; width: 100%;
    text-align: center; font-size: 108px; font-weight: 500;
    line-height: 1; color: var(--ink); letter-spacing: 2px;
  }
  .wordmark__rule {
    position: absolute; left: 205px; top: 378px; width: 460px; height: 3px;
    background: var(--ink);
  }
  .subline {
    position: absolute; left: 0; top: 392px; width: 100%;
    text-align: center; font-size: 33px; letter-spacing: 15px;
    padding-left: 15px; color: var(--ink-soft);
  }
  .product {
    position: absolute; left: 205px; top: 570px; width: 460px;
  }
  .product__type {
    text-align: center; font-size: 23px; font-weight: 700;
    letter-spacing: 5px; color: var(--ink-soft); line-height: 1;
  }
  .rule { height: 1px; background: var(--rule-red); }
  .product__rule-top { margin-top: 12px; }
  .product__specs {
    display: flex; height: 53px; align-items: center;
  }
  .product__spec {
    flex: 1; text-align: center; font-size: 22px; letter-spacing: 2px;
  }
  .product__spec small {
    font-size: 11px; letter-spacing: 1px;
  }
  .unit-stack {
    display: inline-block; vertical-align: middle; font-size: 8px;
    line-height: 1; letter-spacing: 0.5px; margin-left: 4px;
  }
  .unit-stack span { display: block; }
  .unit-stack span:first-child { border-bottom: 1px solid var(--ink); padding-bottom: 1px; margin-bottom: 1px; }
  .product__divider { width: 1px; height: 53px; background: var(--rule-red); }
  .product__origin {
    margin-top: 17px; text-align: center; font-size: 12px;
    letter-spacing: 2.4px; line-height: 17px; font-weight: 500;
  }
  .product__origin-last {
    display: flex; align-items: center; gap: 10px;
  }
  .product__origin-last .rule { flex: 1; }
  .seal {
    position: absolute; left: 745px; top: 613px;
    display: flex; align-items: center; gap: 6px;
  }
  .seal__ring {
    width: 44px; height: 44px; border-radius: 50%;
    border: 2px solid var(--faint);
  }
  .seal__name {
    font-size: 13px; letter-spacing: 2px; color: var(--faint);
  }
</style>
</head>
<body>
  <main class="label">
    <div class="label__band"></div>

    <div class="label__scene" role="img" aria-label="Faint grey illustration of a tall sailing ship on waves behind the wordmark"></div>

    <div class="brand-mark">
      <span class="brand-mark__dot"></span>
      <span class="brand-mark__name">HALMAR</span>
    </div>

    <h1 class="wordmark">HALMAR</h1>
    <div class="wordmark__rule"></div>
    <p class="subline">DISTILLERY</p>

    <section class="product">
      <p class="product__type">HANDCRAFTED RUM</p>
      <div class="rule product__rule-top"></div>
      <div class="product__specs">
        <p class="product__spec">40%<span class="unit-stack"><span>ALC</span><span>VOL</span></span></p>
        <div class="product__divider"></div>
        <p class="product__spec">700<small>ML</small></p>
      </div>
      <div class="rule"></div>
      <p class="product__origin">PROUDLY DISTILLED &amp; CRAFTED WITH QUALITY</p>
      <div class="product__origin product__origin-last" style="margin-top:0">
        <div class="rule"></div>
        <span>IN ESTONIA</span>
        <div class="rule"></div>
      </div>
    </section>

    <div class="seal">
      <span class="seal__ring"></span>
      <span class="seal__name">HALMAR</span>
    </div>
  </main>
</body>
</html>
```